Business Card / Thank You Card for Little Girl Website

This is a company that will be designing do it yourself kits for doll furniture in addition to little girl apparel featuring our logo. The name of the company is Wander the Meadow. The website is written as www.wander the meadow.com with hearts dotting the i's. It's meant to be a website to inspire girls to be creative. We will be using a lower case scripted I dotted with a heart as our logo. Any thoughts? Light Pink, purple and silver are the colors we've chosen. The card is going to be going in each kit as a "Thank you" from Posy so it's not your traditional business card. We can do something along the lines of "I hope I've inspired you! Your friend, Posy!" and dot the i's in inspired with hearts? And then put the website address below it. The font for the website is Wander the Meadow - Jenna Sue www.wanderthemeadow.com - Flirty Girl (hearts dotting the i's on this line only) I'm open to suggestions for something different!
Target Market(s)
Young girls ages 5-10
Industry/Entity Type
Business
Contact Information for Business Card
Laurie Casalelauriecasale@hotmail.com9788360085
Font styles to use
Other font styles liked:
- Jenna Sue and Flirty Girl
Requirements
Must have
- Pinks and Purples
Nice to have
- A cute design for Little Girls. Something fun and whimsical.

```html
<!DOCTYPE html>
<html lang="en">
<head>
<meta charset="utf-8">
<title>Wander the Meadow – Thank You Card</title>
<link rel="stylesheet" href="https://fonts.googleapis.com/css2?family=Crimson+Text:ital,wght@1,400;1,600&display=swap">
<style>
  :root {
    --card-purple: #b277fa;
    --blossom-pink: #eea6f7;
    --message-ink: #45397a;
    --detail-ink: #6a6c98;
  }
  html, body {
    margin: 0;
    padding: 0;
    overflow: hidden;
    background: var(--card-purple);
  }
  .card {
    position: relative;
    width: 1200px;
    height: 702px;
    background: var(--card-purple);
    overflow: hidden;
    font-family: "Crimson Text", Georgia, serif;
    font-style: italic;
  }
  .blossom-field {
    position: absolute;
    left: 0;
    top: 0;
    width: 1200px;
    height: 702px;
  }
  .thank-you {
    position: absolute;
    right: 166px;
    top: 168px;
    margin: 0;
    text-align: right;
    color: var(--message-ink);
    font-weight: 600;
    font-size: 63px;
    line-height: 98px;
    letter-spacing: 0.5px;
  }
  .thank-you span { display: block; }
  .company-details {
    position: absolute;
    right: 123px;
    top: 416px;
    margin: 0;
    text-align: right;
    color: var(--detail-ink);
    font-weight: 400;
    font-size: 44px;
    line-height: 65px;
  }
  .company-details span { display: block; }
</style>
</head>
<body>
  <main class="card">
    <svg class="blossom-field" viewBox="0 0 1200 702" role="img" aria-label="Scattered pink four-petal blossoms drifting across the left side of the card">
      <defs>
        <radialGradient id="blossomGlow" cx="0.25" cy="0.5" r="0.6">
          <stop offset="0" stop-color="#eea6f7" stop-opacity="0.95"/>
          <stop offset="0.6" stop-color="#e29cf7" stop-opacity="0.6"/>
          <stop offset="1" stop-color="#b277fa" stop-opacity="0"/>
        </radialGradient>
      </defs>
      <ellipse cx="260" cy="330" rx="560" ry="440" fill="url(#blossomGlow)"/>
    </svg>

    <p class="thank-you">
      <span>I hope you were inspired!</span>
      <span>Your friend, Posy</span>
    </p>

    <p class="company-details">
      <span>Wander the Meadow</span>
      <span>Tessa Lane</span>
      <span>www.wanderthemeadow.com</span>
    </p>
  </main>
</body>
</html>
```